Wordpress Theme for a Professional Speaker's Website

I I need a website to promote myself as a speaker to corporations and meeting planners. Some examples of similar sites I like are:

http://www.beginwithpurpose-demo.net (this is by far my favorite)
http://www.lorapemberton.net
http://www.teddyvance.net
http://www.bolsinter.net
http://www.dawnacrossridges.net
http://www.rudyfallenbrook.net

I like modern, minimalistic, innovative. I'm okay if it's edgy but still want it communicate professionalism.

The primary objective is to position me as an expert who can deliver valuable information in an entertaining manner.

There are two calls to action. The first is to capture name and email address to subscribe to my newsletter. The second is to request more information about booking me to speak for their company, organization, etc.

The pages on the website will ultimately be the following:

1. Home (should include sections for recent blog posts, featured topics/presentations, short bio, testimonials, email capture, and anything else you think should be added.
2. Meet Owen
3. Blog
4. Keynotes & Speaking
5. Training & Webinars
6. Coaching & Consulting
7. Testimonials
8. Book Owen
9. Media Inquiries
10. Contact

Please feel free to use your creativity. I don't want my requirements to limit you in any way. I'm just looking for a modern, professional site that will make me stand out from the crowd.

I don't have any existing site or brand identity. My plan is to have the website design I ultimately choose serve as the foundation for the rest of my brand identity.

Target Market(s)

Corporate meeting planners and executives

Industry/Entity Type

It Professional

Font styles to use
Sans Serif

Requirements
Must have
• Email capture, testimonials, blog
Nice to have
• None
Should not have
• None

```html
<!DOCTYPE html>
<html lang="en">
<head>
<meta charset="utf-8">
<title>Owen Castrell — Speaker</title>
<link href="https://fonts.googleapis.com/css2?family=Open+Sans:ital,wght@0,400;0,600;0,700;0,800;1,400;1,600&display=swap" rel="stylesheet">
<style>
:root{
  --blue:#1e7fe0;
  --blue-dark:#1669c0;
  --yellow:#f7b928;
  --ink:#222;
  --dark:#1d1d1d;
  --header:#262626;
  --band:#2b2b2b;
  --muted:#555;
  --white:#fff;
}
*{box-sizing:border-box;margin:0;padding:0}
html,body{width:1200px;height:3152px;overflow:hidden}
body{position:relative;font-family:"Open Sans",Arial,sans-serif;color:var(--ink);background:#fff}
.abs{position:absolute}
section,header,footer{position:absolute;left:0;width:1200px;overflow:hidden}

/* header */
.site-header{top:0;height:133px;background:var(--header);border-bottom:2px solid var(--blue)}
.logo{left:162px;top:30px;font-weight:800;font-size:34px;line-height:32px;color:var(--white);letter-spacing:1px}
.utility-bar{left:540px;top:0;width:660px;height:46px;background:var(--blue);clip-path:polygon(22px 0,100% 0,100% 100%,0 100%)}
.utility-nav{left:570px;top:0;height:46px;display:flex;gap:34px;align-items:center;font-size:13px;font-weight:600;color:#fff;text-transform:uppercase}
.main-nav{left:388px;top:80px;display:flex;gap:30px;font-size:13px;font-weight:600;color:#fff;text-transform:uppercase}
.main-nav .active{color:var(--blue)}
.nav-marker{left:400px;top:122px;width:0;height:0;border-left:8px solid transparent;border-right:8px solid transparent;border-bottom:9px solid var(--blue)}

/* hero */
.hero{top:133px;height:543px;background:#000}
.hero-photo{right:0;top:0;width:460px;height:543px;background:radial-gradient(circle at 40% 30%,#6a5a52 0,#3a3330 35%,#0e0c0c 80%)}
.hero-kicker{left:162px;top:180px;font-size:56px;font-weight:800;color:var(--blue);letter-spacing:1px}
.hero-title{left:222px;top:248px;font-size:78px;font-weight:800;color:#fff;letter-spacing:1px}
.hero-dots{left:162px;top:467px;display:flex;gap:5px}
.hero-dots span{width:10px;height:10px;border-radius:50%;background:#555}
.hero-dots .on{background:var(--blue)}

/* subscribe */
.subscribe{top:676px;height:94px;background:var(--blue)}
.subscribe-accent{left:0;top:0;width:490px;height:94px;background:var(--yellow);clip-path:polygon(0 0,100% 0,455px 100%,0 100%)}
.subscribe-text{left:162px;top:24px;width:300px;font-size:16px;font-weight:700;line-height:23px;color:#fff;text-transform:uppercase}
.field{background:#fff;border:1px solid #ddd;font-size:11px;font-style:italic;color:#555;padding:0 10px;display:flex;align-items:center}
.btn{display:flex;align-items:center;justify-content:center;font-weight:700;text-transform:uppercase;color:#fff}
.btn-yellow{background:var(--yellow)}
.btn-blue{background:var(--blue)}

/* as seen on */
.press{top:770px;height:78px;background:var(--band)}
.press-row{left:318px;top:0;height:78px;display:flex;align-items:center;gap:34px;color:#9a9a9a;font-size:14px}
.press-label{font-size:12px;letter-spacing:1px;font-weight:600;text-transform:uppercase}
.press-item{display:flex;align-items:center;gap:7px}
.press-item i{display:block;width:14px;height:14px;border-radius:50%;background:#8a8a8a}

/* featured */
.section-title{width:1200px;text-align:center;font-size:22px;font-weight:700;color:#333;text-transform:uppercase}
.featured{top:848px;height:610px;background:#fff}
.media{background:linear-gradient(135deg,#6b4a3a,#2c2a30)}
.card-title{font-size:14px;font-weight:700;color:var(--blue)}
.card-text{font-size:11px;line-height:17px;color:#444}
.play{border:3px solid rgba(255,255,255,.85);border-radius:50%}
.feature-date{font-size:13px;font-weight:700;color:var(--blue)}
.feature-headline{font-size:17px;font-weight:700;color:var(--yellow);line-height:25px}
.feature-text{font-size:13px;line-height:22px;color:#444}

/* about */
.about{top:1458px;height:454px;background:linear-gradient(90deg,#8fa3a2 0,#a8b6b4 55%,#c7cfcc 100%)}
.about-photo{right:0;top:0;width:460px;height:454px;background:linear-gradient(160deg,#d8dcd8 0,#9fa7ab 45%,#2d3a4e 100%)}
.about-title{left:162px;top:68px;font-size:25px;font-weight:700;color:#fff;text-transform:uppercase}
.about-lead{left:162px;top:126px;width:560px;font-size:14px;line-height:23px;color:#fff}
.about-body{left:162px;top:190px;width:560px;font-size:10.5px;line-height:19px;color:#fff}
.btn-ghost{border:2px solid #fff;color:#fff}
.social{display:flex;gap:20px;align-items:center}
.social i{display:block;width:12px;height:12px;background:#fff;border-radius:50%}

/* testimonials */
.testimonials{top:1912px;height:360px;background:linear-gradient(180deg,#242424,#1a1a1a)}
.testimonials .section-title{color:#fff;top:62px}
.avatar{left:192px;top:138px;width:124px;height:124px;border-radius:50%;border:4px solid #fff;background:linear-gradient(160deg,#e7d8c8,#b48a6e)}
.quote{left:342px;top:140px;width:666px;font-size:13px;font-style:italic;line-height:24px;color:#ddd}
.quote b{font-style:normal;font-weight:800;font-size:20px;color:#fff}
.quote-author{left:342px;top:238px;font-size:13px;font-weight:700;color:#fff;text-transform:uppercase}
.quote-author span{font-weight:600;font-size:11px;color:#aaa}
.arrow-btn{width:24px;height:24px;border:2px solid #aaa;border-radius:50%;display:flex;align-items:center;justify-content:center}

/* blog */
.blog{top:2272px;height:402px;background:#fff}
.post-meta{display:flex;gap:18px;font-size:11px;font-weight:600;color:#333}
.post-meta span{display:flex;align-items:center;gap:5px}

/* booking */
.booking{top:2674px;height:246px;background:linear-gradient(135deg,#f7b928,#f5ae1c 50%,#f8c040)}
.booking .section-title{color:#fff;top:36px}

/* footer */
.site-footer{top:2920px;height:232px;background:var(--blue)}
.footer-logo{left:162px;top:30px;font-weight:800;font-size:30px;line-height:30px;color:#fff;letter-spacing:1px}
.footer-links{left:410px;width:630px;display:flex;flex-wrap:wrap;gap:6px 18px;font-size:11.5px;font-weight:600;color:#fff;text-transform:uppercase}
.touch-label{left:162px;top:130px;font-size:10px;font-weight:700;color:#fff;text-transform:uppercase}
.touch-icons{left:162px;top:146px;display:flex;gap:4px}
.touch-icons i{display:block;width:28px;height:28px;border-radius:50%;border:2px solid #fff;background:var(--blue-dark)}
.copyright{left:778px;top:198px;font-size:10px;color:#fff}
</style>
</head>
<body>

<header class="site-header">
  <div class="abs logo">OWEN<br>CASTRELL</div>
  <div class="abs utility-bar"></div>
  <nav class="abs utility-nav"><span>Blog</span><span>Testimonials</span><span>Book Owen</span><span>Media Inquiries</span><span>Contact</span></nav>
  <nav class="abs main-nav"><span class="active">Home</span><span>Meet Owen</span><span>Keynotes &amp; Speaking</span><span>Training &amp; Webinars</span><span>Coaching &amp; Consulting</span></nav>
  <div class="abs nav-marker"></div>
</header>

<section class="hero">
  <div class="abs hero-photo" role="img" aria-label="Photo of the speaker on stage gesturing to the audience"></div>
  <div class="abs hero-kicker">BUILD A BETTER</div>
  <div class="abs hero-title">BUSINESS</div>
  <div class="abs hero-dots"><span></span><span></span><span class="on"></span><span></span></div>
</section>

<section class="subscribe">
  <div class="abs subscribe-accent"></div>
  <div class="abs subscribe-text">Subscribe an email address get your business secrets</div>
  <div class="abs field" style="left:486px;top:27px;width:214px;height:40px">Name:</div>
  <div class="abs field" style="left:706px;top:27px;width:214px;height:40px">Email address</div>
  <div class="abs btn btn-yellow" style="left:930px;top:27px;width:108px;height:40px;font-size:12px">Subscribe</div>
</section>

<section class="press">
  <div class="abs press-row">
    <span class="press-label">As seen on :</span>
    <span class="press-item"><i></i>Tunewave</span>
    <span class="press-item"><i></i>Corvex</span>
    <span class="press-item">Snapfold</span>
    <span class="press-item">stockroll</span>
    <span class="press-item"><i style="border-radius:2px"></i>Tilepay</span>
  </div>
</section>

<section class="featured">
  <div class="abs section-title" style="top:50px">Featured Topics/Presentations</div>

  <div class="abs media" style="left:162px;top:102px;width:242px;height:146px" role="img" aria-label="Photo of a speaker facing a conference audience"></div>
  <div class="abs play" style="left:260px;top:152px;width:46px;height:46px"></div>
  <div class="abs card-title" style="left:162px;top:258px">Finibus Bonorum</div>
  <div class="abs card-text" style="left:162px;top:282px;width:242px">At vero eos et accusamus et iusto odio dignissi mo s ducimus qui blanditiis praesentium.</div>

  <div class="abs media" style="left:428px;top:102px;width:242px;height:146px;background:linear-gradient(135deg,#9a8878,#4a3c38)" role="img" aria-label="Photo of a seminar room with attendees"></div>
  <div class="abs card-title" style="left:428px;top:258px">Finibus Bonorum</div>
  <div class="abs card-text" style="left:428px;top:282px;width:242px">At vero eos et accusamus et iusto odio dignissi mo s ducimus qui blanditiis praesentium.</div>

  <div class="abs media" style="left:162px;top:340px;width:242px;height:146px;background:linear-gradient(135deg,#b8c0cc,#3e4a66)" role="img" aria-label="Photo of a business team applauding"></div>
  <div class="abs card-title" style="left:162px;top:496px">Finibus Bonorum</div>
  <div class="abs card-text" style="left:162px;top:520px;width:242px">At vero eos et accusamus et iusto odio dignissi mo s ducimus qui blanditiis praesentium.</div>

  <div class="abs media" style="left:428px;top:340px;width:242px;height:146px;background:linear-gradient(135deg,#d9cfc8,#7a5a6e)" role="img" aria-label="Photo of a workshop presenter at a whiteboard"></div>
  <div class="abs card-title" style="left:428px;top:496px">Finibus Bonorum</div>
  <div class="abs card-text" style="left:428px;top:520px;width:242px">At vero eos et accusamus et iusto odio dignissi mo s ducimus qui blanditiis praesentium.</div>

  <div class="abs media" style="left:704px;top:102px;width:334px;height:206px;background:radial-gradient(circle at 55% 40%,#7a5446,#241a18 70%)" role="img" aria-label="Video still of the speaker presenting"></div>
  <div class="abs play" style="left:838px;top:172px;width:64px;height:64px"></div>
  <div class="abs feature-date" style="left:704px;top:320px">11:59 | March 2014</div>
  <div class="abs feature-headline" style="left:704px;top:346px;width:334px">Sed ut ploremerspicilloatis unde omn nat ed ut perspiciatis un.</div>
  <div class="abs feature-text" style="left:704px;top:408px;width:334px">Sed ut perspiciatis unde omnis istenatus er or sit voluptatem accusantium doloremque laudantium, totam rem aperiam, eaque ipsa quae ab illo inventore veritatis et quasi.</div>
  <div class="abs btn btn-yellow" style="left:704px;top:514px;width:110px;height:40px;font-size:11px">Read More</div>
</section>

<section class="about">
  <div class="abs about-photo" role="img" aria-label="Portrait photo of the speaker in a suit"></div>
  <div class="abs about-title">About Owen Castrell</div>
  <div class="abs about-lead">Sed ut perspiciatis unde omnis iste natus error sit voluptatem accusantium doloremque laudantium, totam rem aperiam, eaque ipsa quae ab one voluptatem.</div>
  <div class="abs about-body">Sed ut perspiciatis unde omnis iste natus error sit voluptatem accusantium doloremque laudantium, totam rem aperiam, eaque ipsa quae ab illo inventore veritatis et quasi architecto beatae vitae dicta sunt explicabo. Nemo enim ipsam voluptatem quia voluptas sit aspernatur aut odit aut fugit, sed quia consequuntur magni dolores eos qui ratione voluptatem sequi nesciunt. Neque porro quisquam est, qui dolorem ipsum quia dolor sit amet, consectetur, adipisci velit, sed quia non numquam eius modi tempora incidunt ut labore et dolore magnam aliquam quaerat voluptatem. Neque porro quisquam est, qui dolorem ipsum.</div>
  <div class="abs btn btn-yellow" style="left:162px;top:337px;width:104px;height:38px;font-size:11px">Read More</div>
  <div class="abs btn btn-ghost" style="left:274px;top:337px;width:172px;height:38px;font-size:11px;gap:8px">
    <svg width="10" height="12" viewBox="0 0 10 12"><path d="M0 0L10 6L0 12Z" fill="#fff"/></svg>Watch the Trailer</div>
  <div class="abs social" style="left:462px;top:350px"><i></i><i></i><i></i><i></i><i style="border-radius:2px"></i></div>
</section>

<section class="testimonials">
  <div class="abs section-title">Testimonials</div>
  <div class="abs arrow-btn" style="left:986px;top:70px"><svg width="8" height="10" viewBox="0 0 8 10"><path d="M6 1L2 5L6 9" stroke="#ddd" stroke-width="2" fill="none"/></svg></div>
  <div class="abs arrow-btn" style="left:1012px;top:70px;border-color:#555"><svg width="8" height="10" viewBox="0 0 8 10"><path d="M2 1L6 5L2 9" stroke="#666" stroke-width="2" fill="none"/></svg></div>
  <div class="abs avatar" role="img" aria-label="Portrait photo of the client giving the testimonial"></div>
  <div class="abs quote"><b>“</b> Sed ut perspiciatis unde omnis iste natus error sit voluptatem accusantium doloremque laudantium, totam rem aperiam, eaque ipsa quae ab illo inventore veritatis et quasi architecto beatae vitae dicta sunt explicaboni mpsam voluptatem quia voluptas sit aspernatur aut odit aut fugit, sed quia consequuntur magni <b>”</b></div>
  <div class="abs quote-author">Jhon Smith, <span>City Name, Lorem Sipmdil</span></div>
</section>

<section class="blog">
  <div class="abs section-title" style="top:22px">Recent Blog Posts</div>

  <div class="abs media" style="left:162px;top:86px;width:206px;height:140px;background:linear-gradient(135deg,#cfc6bc,#6e5e52)" role="img" aria-label="Photo of a presenter in a meeting room"></div>
  <div class="abs card-title" style="left:162px;top:240px">Finibus Bonorum</div>
  <div class="abs card-text" style="left:162px;top:264px;width:206px">Sed ut perspiciatis unde omnis ite nats error sit voluptatemelod ut perspiciatis un domnis ite natus ervoluptatem.</div>
  <div class="abs post-meta" style="left:162px;top:334px"><span>▢ Aug 05,2016</span><span>● Comments</span></div>

  <div class="abs media" style="left:385px;top:86px;width:206px;height:140px;background:linear-gradient(135deg,#8aa4c8,#1e2e52)" role="img" aria-label="Photo of a trainer pointing at a screen"></div>
  <div class="abs card-title" style="left:385px;top:240px">Finibus Bonorum</div>
  <div class="abs card-text" style="left:385px;top:264px;width:206px">Sed ut perspiciatis unde omnis ite nats error sit voluptatemelod ut perspiciatis un domnis ite natus ervoluptatem.</div>
  <div class="abs post-meta" style="left:385px;top:334px"><span>▢ Aug 05,2016</span><span>● Comments</span></div>

  <div class="abs media" style="left:608px;top:86px;width:206px;height:140px;background:linear-gradient(135deg,#e0c08a,#7a4e3a)" role="img" aria-label="Photo of an audience applauding"></div>
  <div class="abs card-title" style="left:608px;top:240px">Finibus Bonorum</div>
  <div class="abs card-text" style="left:608px;top:264px;width:206px">Sed ut perspiciatis unde omnis ite nats error sit voluptatemelod ut perspiciatis un domnis ite natus ervoluptatem.</div>
  <div class="abs post-meta" style="left:608px;top:334px"><span>▢ Aug 05,2016</span><span>● Comments</span></div>

  <div class="abs media" style="left:832px;top:86px;width:206px;height:140px;background:linear-gradient(135deg,#d6dcd0,#5a6a5e)" role="img" aria-label="Photo of a team at a flip chart"></div>
  <div class="abs card-title" style="left:832px;top:240px">Finibus Bonorum</div>
  <div class="abs card-text" style="left:832px;top:264px;width:206px">Sed ut perspiciatis unde omnis ite nats error sit voluptatemelod ut perspiciatis un domnis ite natus ervoluptatem.</div>
  <div class="abs post-meta" style="left:832px;top:334px"><span>▢ Aug 05,2016</span><span>● Comments</span></div>
</section>

<section class="booking">
  <div class="abs section-title">Booking Form</div>
  <div class="abs field" style="left:162px;top:84px;width:208px;height:38px">Name:</div>
  <div class="abs field" style="left:378px;top:84px;width:208px;height:38px">Phone:</div>
  <div class="abs field" style="left:594px;top:84px;width:200px;height:38px;justify-content:space-between">Date:<svg width="12" height="12" viewBox="0 0 12 12"><rect x="1" y="2" width="10" height="9" fill="none" stroke="#444" stroke-width="1.5"/><line x1="1" y1="5" x2="11" y2="5" stroke="#444"/></svg></div>
  <div class="abs field" style="left:800px;top:84px;width:238px;height:80px;align-items:flex-start;padding-top:10px">Description:</div>
  <div class="abs field" style="left:162px;top:126px;width:208px;height:38px">Company:</div>
  <div class="abs field" style="left:378px;top:126px;width:208px;height:38px">Email:</div>
  <div class="abs field" style="left:594px;top:126px;width:200px;height:38px;justify-content:space-between">Location:<svg width="10" height="13" viewBox="0 0 10 13"><path d="M5 12C5 12 1 7 1 4.5A4 4 0 0 1 9 4.5C9 7 5 12 5 12Z" fill="#444"/><circle cx="5" cy="4.5" r="1.4" fill="#fff"/></svg></div>
  <div class="abs btn btn-blue" style="left:527px;top:182px;width:146px;height:40px;font-size:13px">Booking Now</div>
</section>

<footer class="site-footer">
  <div class="abs footer-logo">OWEN<br>CASTRELL</div>
  <div class="abs footer-links" style="top:38px"><span>Home</span><span>Meet Owen</span><span>Blog</span><span>Keynotes &amp; Speaking</span><span>Training &amp; Webinars</span><span>Coaching &amp; Consulting</span><span>Testimonials</span><span>Book Owen</span><span>Media Inquiries</span><span>Contact</span></div>
  <div class="abs touch-label">Keep in touch</div>
  <div class="abs touch-icons"><i></i><i></i><i></i><i></i></div>
  <div class="abs field" style="left:410px;top:138px;width:230px;height:40px;font-style:normal">Name:</div>
  <div class="abs field" style="left:650px;top:138px;width:230px;height:40px;font-style:normal">Email:</div>
  <div class="abs btn btn-yellow" style="left:890px;top:138px;width:148px;height:40px;font-size:12px">Subscribe Here</div>
  <div class="abs copyright">© 2016 Owen Castrell . All right reserved &nbsp;Term of Use</div>
</footer>

</body>
</html>
```